Bold & Clean Birch Harbor Stationary Design

Our company, Birch Harbor Advisory Partners needs a business card, letterhead, and envelope design that all also the formatting standards for quillpressdepot.com.

Envelope:
Safe Zone: 9.375" x 4"
Trim Size: 9.5" x 4.15"
Bleed Size: 11.125" 8.625"

Letterhead:
Safe Zone: 10.875" x 8.375"
Trim Size: 11" x 8.5"
Bleed Size: 11.125" x 8.625"

Our mailing address is:
7318 W Larkmoor Rd
Chicago, IL 60647

Please make sure the return address on the envelope is formatted correctly for mailing and the logo is not too large.

Please submit designs in word and PDF form.

Our current letterhead is attached.

We would also like a business card with our existing logo that will meet standards for formatting through Quill Press Depot (quillpressdepot.com).

These standards are:
Safe Zone: 3.375" x 1.875"
Trim Size: 3.5" x 2"
Bleed Size: 3.625" x 2.125"

The business card is going to be for Marcus Lindqvist, President/CEO of Birch Harbor Advisory Partners. Please include the Address, Telephone Number, Cell Phone Number, Fax Number, Email, and Website Address on the card, which are as follows:

7318 W Larkmoor Rd
Chicago, IL 60647

Tel: (773) 591-3072
Cell: (630) 287-6093
Fax: (63) 417-2058
Email: mjl@birchharboradvisory.com
Web: www.birchharboradvisory.com

Please make sure that we can easily change the name of the staff member and job position title ourselves as we will be having cards for individual employees in the future as well.

The back of the card should also have the Birch Harbor logo on it with our services listed:

Financial Planning | Tax | Solutions for Small Businesses

Industry/Entity Type

Accounting

Requirements
Must have
• envelope
• letterhead
• business card
• All meeting standards set out above.

```html
<!DOCTYPE html>
<html lang="en">
<head>
<meta charset="utf-8">
<title>Birch Harbor Advisory Partners – Stationery</title>
<link href="https://fonts.googleapis.com/css2?family=Montserrat:wght@400;500;600&family=Roboto:wght@400;500&display=swap" rel="stylesheet">
<style>
  :root{
    --bg:#6b6b6b;
    --paper:#ffffff;
    --navy:#1f2d5c;
    --orange:#f05a28;
    --mist:#dde1e8;
    --blush:#fde3da;
    --rule:#c9ccd3;
  }
  *{box-sizing:border-box;margin:0;padding:0}
  html,body{width:1200px;height:1200px;overflow:hidden;background:var(--bg)}
  body{position:relative;font-family:'Roboto',Arial,sans-serif;color:var(--navy)}
  .sheet{position:absolute;background:var(--paper);box-shadow:3px 4px 6px rgba(0,0,0,.35);overflow:hidden}

  .brand{display:flex;align-items:center;gap:6px;font-family:'Montserrat',Arial,sans-serif;font-weight:600;color:var(--navy);white-space:nowrap}
  .brand .dot{border-radius:50%;background:var(--orange);flex:none}
  .brand-sub{font-family:'Montserrat',Arial,sans-serif;font-weight:500;letter-spacing:.28em;text-transform:uppercase;color:var(--navy)}

  .faint-disc{position:absolute;border-radius:50%;background:linear-gradient(135deg,var(--mist),var(--blush));opacity:.6}

  /* letterhead */
  .letterhead{left:100px;top:100px;width:500px;height:647px}
  .letterhead .brand{position:absolute;left:42px;top:58px;font-size:17px}
  .letterhead .brand .dot{width:12px;height:12px}
  .letterhead .brand-sub{position:absolute;left:60px;top:82px;font-size:5.5px}
  .letterhead .services{position:absolute;left:42px;top:98px;font-size:7px;font-style:italic;color:var(--navy)}
  .letterhead .contact{position:absolute;left:350px;top:52px;border-left:1px solid var(--orange);padding-left:9px;font-size:7px;line-height:10px}
  .letterhead .contact .addr{color:var(--orange);margin-top:4px}
  .letterhead .faint-disc{left:270px;top:430px;width:250px;height:250px}

  /* business cards */
  .card{left:704px;width:314px;height:179px}
  .card .name{position:absolute;left:19px;font-size:13px;font-weight:500;color:var(--orange)}
  .card .title{position:absolute;left:19px;font-size:8.5px}
  .rows{position:absolute;font-size:9px;line-height:12px;white-space:nowrap}
  .row{display:flex;align-items:center;gap:7px}
  .row svg{width:8px;height:8px;flex:none}
  .row .lbl{color:var(--orange);font-weight:500;margin-right:-3px}
  .row.indent{padding-left:15px}

  .card-dark{top:127px;background:var(--navy);color:#fff}
  .card-dark .name{top:16px}
  .card-dark .title{top:34px;color:#e6e8ef}
  .card-dark .rows{color:#fff}
  .card-dark .rows.left{left:19px;top:128px}
  .card-dark .rows.right{left:150px;top:116px}
  .card-dark .faint-disc{left:170px;top:10px;width:140px;height:140px;background:#2b3a6c;opacity:.8}

  .card-light{top:357px}
  .card-light .name{top:16px}
  .card-light .title{top:34px}
  .card-light .rows.left{left:19px;top:62px;font-size:9.5px}
  .card-light .rows.left .gap{height:5px}
  .card-light .mark{position:absolute;left:200px;top:68px;width:110px;height:110px;border-radius:50%;background:var(--navy);display:flex;align-items:center;justify-content:center}
  .card-light .mark span{font-family:'Montserrat',Arial,sans-serif;font-weight:600;font-size:13px;color:#fff;text-align:center;line-height:15px}

  .card-back{top:587px}
  .card-back .brand{position:absolute;left:50%;top:44px;transform:translateX(-50%);font-size:24px;gap:9px}
  .card-back .brand .dot{width:16px;height:16px}
  .card-back .brand-sub{position:absolute;left:0;right:0;top:82px;text-align:center;font-size:7px}
  .card-back .services{position:absolute;left:0;right:0;top:108px;text-align:center;font-family:'Montserrat',Arial,sans-serif;font-size:8.5px;color:var(--orange)}
  .card-back .addr{position:absolute;left:0;right:0;top:148px;text-align:center;font-family:'Montserrat',Arial,sans-serif;font-size:11px}

  /* envelopes */
  .envelope-front{left:28px;top:839px;width:557px;height:242px}
  .envelope-front .brand{position:absolute;left:16px;top:22px;font-size:14px}
  .envelope-front .brand .dot{width:10px;height:10px}
  .envelope-front .brand-sub{position:absolute;left:32px;top:42px;font-size:4.5px}
  .envelope-front .return{position:absolute;left:16px;top:58px;font-family:'Montserrat',Arial,sans-serif;font-weight:600;font-size:6.5px;line-height:9px}
  .envelope-front .faint-disc{left:410px;top:100px;width:150px;height:150px}

  .envelope-back{left:616px;top:838px;width:558px;height:244px}
  .envelope-back svg.flap{position:absolute;left:0;top:0}
  .envelope-back .seal{position:absolute;left:50%;top:12px;transform:translateX(-50%);width:40px;height:40px;border-radius:50%;border:3px solid var(--navy)}
</style>
</head>
<body>

<section class="sheet letterhead" aria-label="Letterhead">
  <div class="brand"><span class="dot"></span>Birch Harbor</div>
  <div class="brand-sub">Advisory Partners</div>
  <p class="services">Financial Planning | Tax | Solutions for Small Businesses</p>
  <div class="contact">
    <p>(773) 591-3072</p>
    <p>(630) 417-2058</p>
    <p>info@birchharboradvisory.com</p>
    <p>www.birchharboradvisory.com</p>
    <p class="addr">7318 W Larkmoor Rd<br>Chicago, IL 60647</p>
  </div>
  <div class="faint-disc"></div>
</section>

<section class="sheet card card-dark" aria-label="Business card front, dark">
  <div class="faint-disc"></div>
  <p class="name">Marcus Lindqvist</p>
  <p class="title">President/CEO</p>
  <div class="rows left">
    <div class="row"><svg viewBox="0 0 10 10"><rect x="1" y="3" width="8" height="6" rx="1" fill="var(--orange)"/></svg><span class="lbl">T</span>(773) 591-3072</div>
    <div class="row"><svg viewBox="0 0 10 10"><rect x="2.5" y="1" width="5" height="8.5" rx="1" fill="var(--orange)"/></svg><span class="lbl">C</span>(630) 287-6093</div>
    <div class="row"><svg viewBox="0 0 10 10"><rect x="1" y="2" width="8" height="7" rx="1" fill="var(--orange)"/></svg><span class="lbl">F</span>(630) 417-2058</div>
  </div>
  <div class="rows right">
    <div class="row"><svg viewBox="0 0 10 10"><path d="M5 1a3 3 0 0 1 3 3c0 2.2-3 5.5-3 5.5S2 6.2 2 4a3 3 0 0 1 3-3z" fill="var(--orange)"/></svg>7318 W Larkmoor Rd</div>
    <div class="row indent">Chicago, IL 60647</div>
    <div class="row"><svg viewBox="0 0 10 10"><rect x="1" y="2" width="8" height="6" fill="var(--orange)"/></svg>mjl@birchharboradvisory.com</div>
    <div class="row"><svg viewBox="0 0 10 10"><circle cx="5" cy="5" r="4" fill="none" stroke="var(--orange)" stroke-width="1.4"/></svg>www.birchharboradvisory.com</div>
  </div>
</section>

<section class="sheet card card-light" aria-label="Business card front, light">
  <p class="name">Marcus Lindqvist</p>
  <p class="title">President/CEO</p>
  <div class="rows left">
    <div class="row"><svg viewBox="0 0 10 10"><rect x="1" y="3" width="8" height="6" rx="1" fill="var(--orange)"/></svg><span class="lbl">T</span>(773) 591-3072</div>
    <div class="row"><svg viewBox="0 0 10 10"><rect x="2.5" y="1" width="5" height="8.5" rx="1" fill="var(--orange)"/></svg><span class="lbl">C</span>(630) 287-6093</div>
    <div class="row"><svg viewBox="0 0 10 10"><rect x="1" y="2" width="8" height="7" rx="1" fill="var(--orange)"/></svg><span class="lbl">F</span>(630) 417-2058</div>
    <div class="gap"></div>
    <div class="row"><svg viewBox="0 0 10 10"><rect x="1" y="2" width="8" height="6" fill="var(--orange)"/></svg>mjl@birchharboradvisory.com</div>
    <div class="row"><svg viewBox="0 0 10 10"><circle cx="5" cy="5" r="4" fill="none" stroke="var(--orange)" stroke-width="1.4"/></svg>www.birchharboradvisory.com</div>
    <div class="row"><svg viewBox="0 0 10 10"><path d="M5 1a3 3 0 0 1 3 3c0 2.2-3 5.5-3 5.5S2 6.2 2 4a3 3 0 0 1 3-3z" fill="var(--orange)"/></svg>7318 W Larkmoor Rd</div>
    <div class="row indent">Chicago, IL 60647</div>
  </div>
  <div class="mark"><span>Birch<br>Harbor</span></div>
</section>

<section class="sheet card card-back" aria-label="Business card back">
  <div class="brand"><span class="dot"></span>Birch Harbor</div>
  <div class="brand-sub">Advisory Partners</div>
  <p class="services">Financial Planning | Tax | Solutions for Small Businesses</p>
  <p class="addr">7318 W Larkmoor Rd, Chicago, IL 60647</p>
</section>

<section class="sheet envelope-front" aria-label="Envelope front">
  <div class="brand"><span class="dot"></span>Birch Harbor</div>
  <div class="brand-sub">Advisory Partners</div>
  <p class="return">7318 W Larkmoor Rd<br>Chicago, IL 60647</p>
  <div class="faint-disc"></div>
</section>

<section class="sheet envelope-back" aria-label="Envelope back">
  <svg class="flap" width="558" height="80" viewBox="0 0 558 80">
    <path d="M0 0 L58 56 Q64 62 74 62 L484 62 Q494 62 500 56 L558 0" fill="none" stroke="var(--rule)" stroke-width="1"/>
  </svg>
  <div class="seal"></div>
</section>

</body>
</html>
```